Football (soccer) board game app design

Hi,

We are a start up looking for a gameplay design for an app. It is a football trivia app that consists of four main screens; login/register, main navigation, gameplay, question.

OVERALL:
We want our app to be kept in a dark theme. Black or very dark gray is preferable, with a couple of nice colors to give it a stylish touch. We like flat designs, but are open for ideas within the general structure design. The logo can be used in the app, but feel free to improve it you feel you can. In the attached material we have tried to outline some of our ideas and other designs friends have helped us make.

LOGIN/REGISTER:
We want a simple login. Email, password, Chatterly login and the possibility to register a new user. Live search check whether the email is valid and free, and there is also live validation of passwords. If this could be incorporated in the design it would be nice.

MAIN NAVIGATION:
In the main navigation screen we want it to be divided into tabs. A home, my games, my categories and a ranking tab. In the top bar it should be possible to search for categories as well as there should be a button to go to settings.

The Home tab
In the home tab we want a "Quick Play" button, and a list of featured categories. A category can be unlocked or locked, which should be illustrated somehow. When a category is tapped it should divide the block into a left and right tap area, where the user can choose to "Beat to unlock" or "Buy to unlock" if locked and "Practice" or "Challenge Friend" if already unlocked.

The My Games tab
In the my games tab, the current games should be divided into three lists. First "your turn", then "opponents turn" and finally "finished games".

The My Categories tab
This tab should include a list of categories, which the user have bought, but as of design it is fairly similar to the blocks in home tab. So not much different here.

The Ranking tab
Ranking should show a set of leaderboards; Today, This Week, This Month, etc. The row in a leaderboard should have teamname and a win percentage.

GAMEPLAY:
The gameplay is inspired by an old football (soccer) board game from the 1950's, and our gameplay consists of three core elements; a football (soccer) pitch, 11 players and a scoreboard.

The football (soccer) pitch
What we need is a pitch seen from behind the goal line. The important issue here, is the perspective, as we want 11 players on the field formed as a 4-3-3 formation, being 1 goalkeeper, 4 defenders, 3 midfielder and 3 strikers. They should all be touchable without overlap. In the other end we want a goal that should be touchable as well. The goal in the nearest end do not have to be visible. Due to the perspective of the field and the fact that players and goal should be touchable, of course give you the opportunity to play around with the proportions of both players and goal. We rather want a large goal being out of proportions, than a small goal with a tiny tap area. Around the field (sidelines and beside the goal) we would like advertising banners like seen on a real stadium.

The players
As mentioned we want 11 players in a 4-3-3 formation. The players should be attached to the board with springs as seen on some of the very old board games, where you could flick the player to pass the ball. This also means that we want the players to be placed in an indentation for the ball to fall into and it would be very cool if you could illustrate the player with the ball, as being pulled back to one of the sides, just enough to see the ball at his feet. The players should be large enough for a user to tap them, hence it would also be beneficial if they are not overlapping. For a start we would like to see the players in a blue shirt and white shorts (socks are not necessary as they are placed on a spring).

Scoreboard
On the scoreboard above the field, we need information such as the names of the two teams (could be FC Brightmoor and Tall Oak Rovers), the score (2-1), minutes played (42), and which half (1st). We also want a progress bar that illustrates how many moves you have used ranging from 0-5. The scoreboard could be inspired from the ones seen around stadiums across the world, but feel free to improvise.

What We Are Looking for
We are looking for full PSD and AI files so we can use them to make minor changes like colors on shirts and shorts, colors on pitch, etc. We really want you to be innovative and inspire us, as we are not designers ourselves. In the attached files, we have tried to sketch out a design that covers our initial ideas. We are looking for a professional look, and having the players and field look like a real board game would just be awesome. A combination of the look from the realistic pitch with advertising banners around it, the idea of our spring-players and the initial thoughts of a design illustrated in our sketch, should help you along. Flat design, cartoonish or somewhere in between is up to you, we just want you to impress and make "wow"-feeling.

QUESTION:
The final screen should display a question with four possible answers. There should be a green/checkmark when correct answer, and a red/cross if incorrect.

That's all. We are looking very much forward to see your designs!
Updates

Hi all,

We have changed the terms of the contest to now have a guaranteed payment, and we are really looking forward to see your designs! Good luck.

/ Mikkel and Anders

By request we have now uploaded an AI-file with the logo for you to play around with. We are looking forward to see your designs.

/ Mikkel and Anders

Reason: Hi designers, We are really happy with the progress being made, and are looking forward to see some of the designs that are still work in progress. However the amount of designs received, has not reached our expectations yet. Therefore we are extending the deadline for seven more days, so designers, that are still working on their designs can continue their work without a stressing deadline in the horizon. Good luck to all of you. We are looking very much forward to see, what you are able to produce. Best regards, Mikkel and Anders

Reason: Hi all, We still have a lot of designers in the competition , who are battling to finish their designs, therefore we have decided to extend the deadline once more. Good luck to all of you!

Target Market(s)

Football (soccer) fans

Industry/Entity Type

Advertising

```html
<!DOCTYPE html>
<html lang="en">
<head>
<meta charset="utf-8">
<title>Quizkicker – Sign Up</title>
<link rel="stylesheet" href="https://fonts.googleapis.com/css2?family=Open+Sans:wght@300;400;600&family=Roboto:wght@300;400&display=swap">
<style>
  :root {
    --bg: #050708;
    --glow: #1f8fb8;
    --haze: #2a2f33;
    --brand-dim: #4a5257;
    --panel: #0a0d10;
    --panel-line: #2d6f86;
    --field-line: #3a8aa3;
    --field-active: #16a8ea;
    --text: #ffffff;
    --text-soft: #e6eef2;
    --kbd-bg: #d1d5db;
    --key: #ffffff;
    --key-dark: #acb3bc;
    --key-shadow: #898c91;
    --key-text: #000000;
    --go: #1a82fb;
  }
  * { box-sizing: border-box; margin: 0; padding: 0; }
  html, body { width: 677px; height: 1200px; overflow: hidden; background: var(--bg); }
  .screen { position: relative; width: 677px; height: 1200px; overflow: hidden; background: var(--bg); font-family: "Open Sans", sans-serif; color: var(--text); }

  .backdrop { position: absolute; inset: 0; }

  .status-bar { position: absolute; top: 0; left: 0; width: 677px; height: 45px; font-family: "Roboto", sans-serif; font-size: 25px; color: var(--text); }
  .status-bar .left { position: absolute; left: 10px; top: 8px; display: flex; align-items: center; gap: 8px; }
  .signal { display: flex; gap: 3px; }
  .signal i { width: 11px; height: 11px; border-radius: 50%; border: 1.5px solid var(--text); display: block; }
  .signal i.on { background: var(--text); }
  .status-bar .time { position: absolute; left: 0; right: 0; top: 8px; text-align: center; font-weight: 400; }
  .status-bar .right { position: absolute; right: 12px; top: 8px; display: flex; align-items: center; gap: 8px; }
  .battery { width: 50px; height: 20px; border: 2px solid var(--text); border-radius: 4px; position: relative; padding: 2px; }
  .battery::after { content: ""; position: absolute; right: -6px; top: 5px; width: 3px; height: 7px; background: var(--text); }
  .battery span { display: block; width: 22%; height: 100%; background: var(--text); }

  .brand { position: absolute; top: 160px; left: 0; width: 677px; text-align: center; font-family: "Open Sans", sans-serif; font-weight: 300; font-size: 76px; line-height: 90px; color: var(--brand-dim); }

  .signup-panel { position: absolute; left: 41px; top: 311px; width: 596px; height: 900px; background: var(--panel); border: 2px solid var(--panel-line); }
  .signup-panel .close { position: absolute; right: 20px; top: 14px; font-size: 34px; font-weight: 300; line-height: 1; }
  .signup-panel h1 { position: absolute; top: 40px; left: 0; right: 0; text-align: center; font-weight: 400; font-size: 40px; letter-spacing: 1px; }
  .field { position: absolute; left: 43px; width: 507px; height: 55px; border: 2px solid var(--field-line); font-size: 28px; padding-left: 18px; line-height: 51px; color: var(--text-soft); }
  .field.active { background: var(--field-active); border-color: var(--field-active); color: var(--text); }

  .keyboard { position: absolute; left: 0; top: 767px; width: 677px; height: 433px; background: var(--kbd-bg); font-family: "Roboto", sans-serif; color: var(--key-text); }
  .key { position: absolute; width: 59px; height: 85px; background: var(--key); border-radius: 10px; box-shadow: 0 2px 0 var(--key-shadow); display: flex; align-items: center; justify-content: center; font-size: 44px; font-weight: 300; }
  .key.dark { background: var(--key-dark); }
  .key.small { font-size: 32px; }
  .key.go { background: var(--go); color: var(--text); font-size: 34px; }
</style>
</head>
<body>
<div class="screen">
  <svg class="backdrop" width="677" height="1200" viewBox="0 0 677 1200" aria-hidden="true">
    <defs>
      <linearGradient id="beam-left" x1="0" y1="0" x2="1" y2="0">
        <stop offset="0" stop-color="#1f8fb8" stop-opacity=".15"/>
        <stop offset="1" stop-color="#1f8fb8" stop-opacity=".9"/>
      </linearGradient>
      <linearGradient id="beam-right" x1="1" y1="0" x2="0" y2="0">
        <stop offset="0" stop-color="#1f8fb8" stop-opacity=".15"/>
        <stop offset="1" stop-color="#1f8fb8" stop-opacity=".9"/>
      </linearGradient>
      <radialGradient id="haze" cx="0.5" cy="0.5" r="0.5">
        <stop offset="0" stop-color="#2a2f33" stop-opacity=".8"/>
        <stop offset="1" stop-color="#2a2f33" stop-opacity="0"/>
      </radialGradient>
    </defs>
    <ellipse cx="30" cy="520" rx="90" ry="130" fill="url(#haze)"/>
    <ellipse cx="650" cy="520" rx="80" ry="120" fill="url(#haze)"/>
    <path d="M0 214 L95 278" stroke="url(#beam-left)" stroke-width="3"/>
    <path d="M677 214 L582 278" stroke="url(#beam-right)" stroke-width="3"/>
    <path d="M0 605 L41 568" stroke="#1f8fb8" stroke-opacity=".5" stroke-width="2"/>
    <path d="M677 605 L637 568" stroke="#1f8fb8" stroke-opacity=".5" stroke-width="2"/>
  </svg>

  <div class="status-bar">
    <div class="left">
      <div class="signal"><i class="on"></i><i class="on"></i><i class="on"></i><i></i><i></i></div>
      <span>LYNX</span>
      <svg width="28" height="20" viewBox="0 0 28 20" aria-hidden="true"><path d="M2 7 Q14 -3 26 7 M6 11 Q14 4 22 11 M10 15 Q14 11 18 15" fill="none" stroke="#fff" stroke-width="2.5"/><circle cx="14" cy="18" r="2" fill="#fff"/></svg>
    </div>
    <div class="time">4:21 PM</div>
    <div class="right">
      <svg width="14" height="24" viewBox="0 0 14 24" aria-hidden="true"><path d="M2 6 L12 16 L7 21 L7 3 L12 8 L2 18" fill="none" stroke="#fff" stroke-width="2"/></svg>
      <span>22%</span>
      <div class="battery"><span></span></div>
    </div>
  </div>

  <div class="brand">quizkicker</div>

  <section class="signup-panel">
    <div class="close">×</div>
    <h1>SIGN UP</h1>
    <div class="field active" style="top:129px">First Name</div>
    <div class="field" style="top:217px">Last Name</div>
    <div class="field" style="top:303px">Email</div>
    <div class="field" style="top:391px">Password</div>
  </section>

  <div class="keyboard">
    <div class="key" style="left:4px;top:12px">Q</div>
    <div class="key" style="left:72px;top:12px">W</div>
    <div class="key" style="left:140px;top:12px">E</div>
    <div class="key" style="left:207px;top:12px">R</div>
    <div class="key" style="left:275px;top:12px">T</div>
    <div class="key" style="left:343px;top:12px">Y</div>
    <div class="key" style="left:410px;top:12px">U</div>
    <div class="key" style="left:478px;top:12px">I</div>
    <div class="key" style="left:546px;top:12px">O</div>
    <div class="key" style="left:614px;top:12px">P</div>

    <div class="key" style="left:38px;top:118px">A</div>
    <div class="key" style="left:106px;top:118px">S</div>
    <div class="key" style="left:174px;top:118px">D</div>
    <div class="key" style="left:241px;top:118px">F</div>
    <div class="key" style="left:309px;top:118px">G</div>
    <div class="key" style="left:377px;top:118px">H</div>
    <div class="key" style="left:444px;top:118px">J</div>
    <div class="key" style="left:512px;top:118px">K</div>
    <div class="key" style="left:580px;top:118px">L</div>

    <div class="key dark" style="left:7px;top:226px;width:83px">
      <svg width="34" height="32" viewBox="0 0 34 32" aria-hidden="true"><path d="M17 3 L31 17 L23 17 L23 29 L11 29 L11 17 L3 17 Z" fill="none" stroke="#000" stroke-width="2"/></svg>
    </div>
    <div class="key" style="left:108px;top:226px">Z</div>
    <div class="key" style="left:176px;top:226px">X</div>
    <div class="key" style="left:243px;top:226px">C</div>
    <div class="key" style="left:311px;top:226px">V</div>
    <div class="key" style="left:379px;top:226px">B</div>
    <div class="key" style="left:446px;top:226px">N</div>
    <div class="key" style="left:514px;top:226px">M</div>
    <div class="key dark" style="left:587px;top:226px;width:83px">
      <svg width="44" height="30" viewBox="0 0 44 30" aria-hidden="true"><path d="M14 3 L41 3 L41 27 L14 27 L2 15 Z" fill="none" stroke="#000" stroke-width="2"/><path d="M21 9 L33 21 M33 9 L21 21" stroke="#000" stroke-width="2"/></svg>
    </div>

    <div class="key dark small" style="left:7px;top:334px;width:77px">123</div>
    <div class="key dark" style="left:90px;top:334px;width:75px">
      <svg width="36" height="36" viewBox="0 0 36 36" aria-hidden="true"><g fill="none" stroke="#000" stroke-width="2"><circle cx="18" cy="18" r="15"/><ellipse cx="18" cy="18" rx="6" ry="15"/><path d="M3 18 H33 M6 10 H30 M6 26 H30"/></g></svg>
    </div>
    <div class="key dark" style="left:171px;top:334px;width:66px">
      <svg width="24" height="40" viewBox="0 0 24 40" aria-hidden="true"><g fill="none" stroke="#000" stroke-width="2"><rect x="6" y="2" width="12" height="22" rx="6"/><path d="M2 18 Q2 31 12 31 Q22 31 22 18 M12 31 V38 M6 38 H18"/></g></svg>
    </div>
    <div class="key small" style="left:248px;top:334px;width:147px">space</div>
    <div class="key small" style="left:406px;top:334px;width:102px">.com</div>
    <div class="key go" style="left:517px;top:334px;width:153px">Go</div>
  </div>
</div>
</body>
</html>
```